Letterhead Design Project

I need a simple, clean and corporate letterhead & follow-on letterhead.
The follow-on letterhead should just have the logo only.
Final File Specs:
Full Bleed Size (starting document size)
213 x 300 mm
2517 x 3544 pixels
* Finished artwork should use the full bleed dimensions for best results.
Document Trim Size (final size after being cut)
210 x 297 mm
2480 x 3508 pixels
* Please be sure to keep all text within the safe margin.
Resolution 300 DPI
Accepted file types:-
Adobe Acrobat 9 Document (*.pdf) (recommended)
Adobe Illustrator CS3 Artwork (*.ai) (recommended)
Adobe Photoshop CS3 Image (*.psd) (recommended)
Bitmap Image (*.bmp)
GIF Image (*.gif)
JPEG Image (*.jpg,*.jpeg)
Microsoft PowerPoint 2010 Document (*.ppt)
Microsoft Publisher 2010 Document (*.pub)
Microsoft Word 2010 Document (*.doc)
PCX Image (*.pcx)
PICT Image (*.pic,*.pict,*.pct)
PNG Image (*.png)
PostScript Document (*.ps)
TIF Image (*.tif,*.tiff)
Windows Enhanced Metafile (*.emf)
Windows Metafile (*.wmf)
Requirements
Must have
- My letterhead must have:-
- Logo
- ACN - 482 617 309
- address - Suite 8, 51 Hartwell Ave, Coogee, NSW 2034
- phone - (02) 8371 5926
- fax - (02) 8352 6149
- email - info@brantorguard.com.au
- web - www.brantorguard.com.au
Follow-on letterhead should have the logo only

```html
<!DOCTYPE html>
<html lang="en">
<head>
<meta charset="utf-8">
<title>Brantor Asbestos &amp; Safety – Letterhead Set</title>
<link rel="stylesheet" href="https://fonts.googleapis.com/css2?family=Montserrat:wght@700&family=Questrial&display=swap">
<style>
  :root {
    --navy: #0b1166;
    --lime: #9cf41c;
    --paper: #ffffff;
    --ink-light: #ffffff;
  }
  * { margin: 0; padding: 0; box-sizing: border-box; }
  html, body {
    width: 1200px;
    height: 2880px;
    overflow: hidden;
    background: var(--paper);
  }
  .sheet-set { position: relative; width: 1200px; height: 2880px; }
  .sheet {
    position: absolute;
    left: 0;
    width: 1200px;
    background: var(--paper);
    overflow: hidden;
  }
  .sheet--main { top: 0; height: 1430px; }
  .sheet--follow { top: 1445px; height: 1435px; }
  .sheet__swoosh { position: absolute; top: 0; left: 0; width: 1200px; height: 560px; }
  .sheet__band {
    position: absolute;
    left: 0;
    bottom: 0;
    width: 100%;
    height: 50px;
    background: var(--lime);
  }
  .brand {
    position: absolute;
    left: 52px;
    top: 78px;
  }
  .brand__name {
    display: block;
    font-family: "Montserrat", sans-serif;
    font-weight: 700;
    font-size: 64px;
    line-height: 1;
    color: var(--navy);
  }
  .brand__tagline {
    display: block;
    margin-top: 14px;
    font-family: "Montserrat", sans-serif;
    font-weight: 700;
    font-size: 26px;
    letter-spacing: 0.5px;
    color: var(--navy);
  }
  .contact {
    position: absolute;
    top: 62px;
    right: 46px;
    text-align: right;
    font-family: "Questrial", sans-serif;
    font-size: 18px;
    line-height: 22.5px;
    color: var(--ink-light);
    list-style: none;
  }
</style>
</head>
<body>
<main class="sheet-set">

  <section class="sheet sheet--main" aria-label="Letterhead first page">
    <svg class="sheet__swoosh" viewBox="0 0 1200 560" aria-hidden="true">
      <path d="M192 0 C 690 40, 1080 200, 1200 516 L1200 0 Z" fill="var(--navy)"/>
    </svg>
    <div class="brand">
      <span class="brand__name">Brantor</span>
      <span class="brand__tagline">ASBESTOS &amp; SAFETY</span>
    </div>
    <ul class="contact">
      <li>ACN 482 617 309</li>
      <li>Suite 8, 51 Hartwell Ave, Coogee, NSW 2034</li>
      <li>T: (02) 8371 5926</li>
      <li>F: (02) 8352 6149</li>
      <li>info@brantorguard.com.au</li>
      <li>www.brantorguard.com.au</li>
    </ul>
    <div class="sheet__band"></div>
  </section>

  <section class="sheet sheet--follow" aria-label="Follow-on letterhead">
    <svg class="sheet__swoosh" viewBox="0 0 1200 560" aria-hidden="true">
      <path d="M192 0 C 690 40, 1080 200, 1200 516 L1200 0 Z" fill="var(--navy)"/>
    </svg>
    <div class="brand">
      <span class="brand__name">Brantor</span>
      <span class="brand__tagline">ASBESTOS &amp; SAFETY</span>
    </div>
    <div class="sheet__band"></div>
  </section>

</main>
</body>
</html>
```